Business Card for Quillmark Ledger - A cannabis publication for executives.

I'd like some business cards for Quillmark Ledger. The logo is done (great job!) and I need a card design I will use with PRINTLY. I made it a short project to allow time for printing before an event. These will be standard sized cards (final artwork size 3.66" x 2.16" at 300dpi) with a final card size of 3.5" x 2.0". (See PRINTLY.com if you need more info.) I might try rounded corners but am not sure yet. I think the design will work okay with rounded.

Quillmark Ledger will be a bi-weekly publication for the cannabis industry. It is targeted to investors and industry executives, not consumers or pot smokers. So our market is more B2B. However I am open to creativity and making the card something people remark on.

My contact for card:

Dana Merrow
Founder/CEO
dana@quillmarkledger.example

2740 Harlow Avenue
Boston MA 02135
(617)555-0194

Target Market(s)

Executives, Industry people and investors in the Cannabis sector.

Contact Information for Business Card

PRINTLY does do double sided and the second side can be the same or different images. Only one side is required but use of the second side would be a bonus.

Font styles to use
Serif
Sans Serif
Decorative

Colors

Designer to choose colors to be used in the design.

Requirements
Must have
• Logo, contact info
Nice to have
• Style and design to make the card stand out in a crowd.

```html
<!DOCTYPE html>
<html lang="en">
<head>
<meta charset="utf-8">
<title>Quillmark Ledger — Business Card</title>
<link rel="stylesheet" href="https://fonts.googleapis.com/css2?family=Open+Sans:wght@400;600&display=swap">
<style>
  :root {
    --brand-blue: #1557a8;
    --brand-green: #4f8f1e;
    --ink: #1c1c1c;
    --card: #ffffff;
    --backdrop: #8a8a8a;
  }
  * { margin: 0; padding: 0; box-sizing: border-box; }
  html, body { width: 1200px; height: 1200px; overflow: hidden; }
  body {
    background: var(--backdrop);
    font-family: "Open Sans", sans-serif;
    display: flex;
    flex-direction: column;
    align-items: center;
    justify-content: center;
    gap: 80px;
  }
  .card {
    width: 840px;
    height: 480px;
    background: var(--card);
    box-shadow: 0 6px 18px rgba(0,0,0,0.25);
    position: relative;
  }
  /* Front */
  .card-front {
    display: flex;
    align-items: center;
    justify-content: center;
    gap: 22px;
  }
  .brand-dot {
    width: 58px;
    height: 58px;
    border-radius: 50%;
    background: var(--brand-green);
  }
  .brand-name {
    font-size: 54px;
    font-weight: 600;
    color: var(--brand-blue);
    letter-spacing: 0.5px;
  }
  /* Back */
  .card-back {
    display: flex;
    align-items: center;
    padding-top: 0;
  }
  .identity {
    width: 335px;
    text-align: right;
    padding-right: 24px;
    align-self: center;
    margin-top: -60px;
  }
  .person-name {
    font-size: 38px;
    font-weight: 400;
    color: var(--brand-blue);
    letter-spacing: 1px;
    line-height: 1.1;
  }
  .person-title {
    font-size: 20px;
    color: var(--ink);
    margin-top: 2px;
  }
  .divider {
    width: 2px;
    height: 150px;
    background: var(--brand-green);
    margin-top: -10px;
  }
  .contact {
    list-style: none;
    padding-left: 22px;
    font-size: 23px;
    color: var(--ink);
    line-height: 1.25;
    margin-top: 10px;
  }
  .contact li {
    display: flex;
    align-items: flex-start;
    gap: 10px;
  }
  .contact li + li { margin-top: 2px; }
  .contact .address { margin-top: 10px; }
  .contact svg {
    width: 22px;
    height: 22px;
    flex: none;
    margin-top: 4px;
    fill: var(--brand-green);
  }
</style>
</head>
<body>

  <section class="card card-front" aria-label="Card front">
    <span class="brand-dot" aria-hidden="true"></span>
    <span class="brand-name">Quillmark Ledger</span>
  </section>

  <section class="card card-back" aria-label="Card back">
    <div class="identity">
      <p class="person-name">DANA MERROW</p>
      <p class="person-title">Founder/CEO</p>
    </div>
    <div class="divider" aria-hidden="true"></div>
    <ul class="contact">
      <li>
        <svg viewBox="0 0 24 24" aria-hidden="true"><path d="M3 7c0-2 4-4 9-4s9 2 9 4v2h-5V7.5c-1-.5-2.5-.8-4-.8s-3 .3-4 .8V9H3z"/><path d="M6 11h12l2 9H4z M12 13a3 3 0 1 0 0 6 3 3 0 0 0 0-6z"/></svg>
        <span>(617)555-0194</span>
      </li>
      <li>
        <svg viewBox="0 0 24 24" aria-hidden="true"><path d="M2 5h20v14H2z M3.5 6.5 12 13l8.5-6.5z" fill-rule="evenodd"/></svg>
        <span>dana@quillmarkledger.example</span>
      </li>
      <li class="address">
        <svg viewBox="0 0 24 24" aria-hidden="true"><path d="M12 2a7 7 0 0 0-7 7c0 5 7 13 7 13s7-8 7-13a7 7 0 0 0-7-7zm0 4a3 3 0 1 1 0 6 3 3 0 0 1 0-6z" fill-rule="evenodd"/></svg>
        <span>2740 Harlow Avenue<br>Boston MA 02135</span>
      </li>
    </ul>
  </section>

</body>
</html>
```